Business card for real estate agent / office

We're looking for a new business card. We want something that is pretty clean, modern and sleek. Something that also tells people that we are a new age company...cutting edge. Although real estate has been done a certain way the last 100 years, we have energy and vibrance. Company name is Bright Harbor Properties. info can be found here: http://www.bhprealestate.example/

needs to include: Name, title, phone number, email. our license number also needs to be displayed somewhere.

Target Market(s)

25-55 homeowners or potential homeowners

Industry/Entity Type

Business

Contact Information for Business Card

we need business card designs for real estate agent / office

Font styles to use
Serif

Requirements
Must have
• needs to include: Name, title, phone number, email. our license number also needs to be displayed somewhere and company name.
Nice to have
• placement area for photo

```html
<!DOCTYPE html>
<html lang="en">
<head>
<meta charset="utf-8">
<title>Bright Harbor Properties – Business Card</title>
<link href="https://fonts.googleapis.com/css2?family=Source+Sans+3:wght@400;600;700&display=swap" rel="stylesheet">
<style>
  :root {
    --navy: #0f4a73;
    --green: #5cb947;
    --ink: #2a2a2a;
    --paper: #ffffff;
    --ghost: #e4e4e4;
    --backdrop: #3a3533;
  }
  * { margin: 0; padding: 0; box-sizing: border-box; }
  html, body {
    width: 1200px; height: 844px; overflow: hidden;
    background: var(--backdrop);
    font-family: "Source Sans 3", "Helvetica Neue", Arial, sans-serif;
  }
  .stage { position: relative; width: 1200px; height: 844px; }
  .card {
    position: absolute; top: 272px;
    width: 520px; height: 300px;
    background: var(--paper);
    overflow: hidden;
  }
  .card--contact { left: 50px; }
  .card--brand { left: 630px; }

  /* contact side */
  .band-top { position: absolute; left: 0; top: 0; width: 100%; height: 12px; background: var(--navy); }
  .band-bottom { position: absolute; left: 0; bottom: 0; width: 100%; height: 16px; background: var(--green); }
  .ghost-square {
    position: absolute; left: 18px; bottom: 40px;
    width: 120px; height: 120px; background: var(--ghost);
  }
  .contact {
    position: absolute; left: 170px; top: 52px; width: 300px;
    text-align: center; color: var(--ink);
  }
  .contact__name { font-size: 26px; font-weight: 700; color: var(--navy); line-height: 1.1; }
  .contact__name .surname { color: var(--green); }
  .contact__title { font-size: 15px; margin-top: 2px; }
  .contact__license { font-size: 17px; font-weight: 700; margin-top: 22px; }
  .contact__license .label { color: var(--navy); }
  .contact__lines { font-size: 16px; margin-top: 18px; line-height: 1.5; }

  /* brand side */
  .tab { position: absolute; width: 30px; height: 52px; background: var(--navy); }
  .tab--left { left: 0; top: 126px; border-right: 5px solid var(--green); }
  .tab--right { right: 0; top: 26px; border-left: 5px solid var(--green); }
  .brand {
    position: absolute; left: 0; top: 108px; width: 100%;
    display: flex; align-items: center; justify-content: center; gap: 12px;
  }
  .brand__square { width: 22px; height: 22px; background: var(--green); }
  .brand__name { font-size: 30px; font-weight: 700; color: var(--navy); }
  .tagline {
    position: absolute; left: 0; top: 186px; width: 100%;
    text-align: center; font-size: 15px; font-weight: 700;
    letter-spacing: 0.5px; color: var(--navy);
  }
</style>
</head>
<body>
<main class="stage">
  <section class="card card--contact">
    <div class="band-top"></div>
    <div class="ghost-square"></div>
    <div class="contact">
      <p class="contact__name">Daniel <span class="surname">Okafor</span></p>
      <p class="contact__title">Real Estate Broker, Realtor, MBA</p>
      <p class="contact__license"><span class="label">CA BRE</span> #02917354</p>
      <div class="contact__lines">
        <p>310.555.0142</p>
        <p>dan@brightharborprop.example</p>
        <p>www.brightharborprop.example</p>
      </div>
    </div>
    <div class="band-bottom"></div>
  </section>

  <section class="card card--brand">
    <div class="tab tab--right"></div>
    <div class="tab tab--left"></div>
    <div class="brand">
      <span class="brand__square"></span>
      <span class="brand__name">Bright Harbor Properties</span>
    </div>
    <p class="tagline">WE GREATLY APPRECIATE YOUR REFERRALS</p>
  </section>
</main>
</body>
</html>
```